Ferrant Valley Zoning Council Business Cards

We're looking for a business card design, simple as that. We're a local government agency that mainly performs building code enforcement, transportation planning, floodplain management, and GIS for Tobelle Parish in Louisiana, and other surround parishes. So you're not having to Google anything, GIS is, at it's core, mapping. Building Code Enforcement is just that, nothing more. Floodplain Management is to make sure the public is within what the government

Contact Information for Business Card

Our Address is

517 Marwick Street
Alexandria, LA 71489

Our phone is 3185529137
Our fax is 3185529142
Our website is www.fvzc.info
My email is dana@fvzc.info

Font styles to use
Serif
Sans Serif

Colors

Designer to choose colors to be used in the design.

Requirements
Must have
• I'm attaching our logo(several versions) that must be incorporated. The design should fit well with our existing logo. I can send photoshop files for our logo if needed. If possible, I'd like to be able to add names/info to each card for all of our employees once this is done.
Nice to have
• The Louisiana state seal is a bonus, and isn't specifically required.

```html
<!DOCTYPE html>
<html lang="en">
<head>
<meta charset="UTF-8">
<title>Ferrant Valley Zoning Council – Business Cards</title>
<link rel="stylesheet" href="https://fonts.googleapis.com/css2?family=Arimo:wght@400;700&display=swap">
<style>
  :root {
    --page: #ffffff;
    --card: #141414;
    --ink: #ffffff;
    --accent: #7bafd4;
    --mark: #3a5ba9;
    --ghost: #1b1b1b;
  }
  * { margin: 0; padding: 0; box-sizing: border-box; }
  html, body {
    width: 1000px; height: 1200px; overflow: hidden;
    background: var(--page);
    font-family: "Arimo", Arial, sans-serif;
    color: var(--ink);
  }
  .sheet { position: relative; width: 1000px; height: 1200px; }
  .card {
    position: absolute; left: 101px; width: 800px; height: 457px;
    background: var(--card); overflow: hidden;
  }
  .card--front { top: 64px; }
  .card--back { top: 556px; }

  .brand { position: absolute; display: flex; align-items: flex-start; }
  .brand__square { background: var(--mark); flex: none; }
  .brand__text { font-weight: 700; color: var(--ink); }
  .brand__acronym { display: block; line-height: 1; letter-spacing: 1px; }
  .brand__name { display: block; line-height: 1.2; }

  .card--front .brand { left: 79px; top: 189px; }
  .card--front .brand__square { width: 66px; height: 66px; margin: 2px 12px 0 0; }
  .card--front .brand__acronym { font-size: 68px; }
  .card--front .brand__name { font-size: 12px; margin-top: 4px; }

  .divider {
    position: absolute; left: 428px; top: 153px;
    width: 3px; height: 201px; background: var(--accent);
  }
  .contact { position: absolute; left: 471px; top: 143px; list-style: none; }
  .contact__item {
    display: flex; align-items: center; height: 38.5px;
    font-size: 21px;
  }
  .contact__icon { width: 18px; height: 18px; margin-right: 36px; flex: none; }
  .address {
    position: absolute; left: 473px; top: 307px;
    font-size: 21px; line-height: 26px; font-style: normal;
  }

  .ghost {
    position: absolute; left: 10px; top: 60px;
    font-size: 330px; font-weight: 700; line-height: 1;
    color: var(--ghost); letter-spacing: 4px;
  }
  .card--back .brand { left: 179px; top: 158px; }
  .card--back .brand__square { width: 116px; height: 116px; margin: 6px 18px 0 0; }
  .card--back .brand__acronym { font-size: 110px; }
  .card--back .brand__name { font-size: 19px; margin-top: 6px; }
</style>
</head>
<body>
<main class="sheet">
  <section class="card card--front" aria-label="Card front">
    <div class="brand">
      <span class="brand__square"></span>
      <div class="brand__text">
        <span class="brand__acronym">FVZC</span>
        <span class="brand__name">Ferrant Valley Zoning Council</span>
      </div>
    </div>
    <div class="divider"></div>
    <ul class="contact">
      <li class="contact__item">
        <svg class="contact__icon" viewBox="0 0 24 24" fill="var(--accent)" aria-hidden="true"><path d="M6.6 10.8a15.1 15.1 0 0 0 6.6 6.6l2.2-2.2c.3-.3.7-.4 1-.2 1.1.4 2.300.6 3.6.6.6 0 1 .4 1 1V20c0 .6-.4 1-1 1C10.6 21 3 13.4 3 4c0-.6.4-1 1-1h3.5c.6 0 1 .4 1 1 0 1.3.2 2.5.6 3.6.1.3 0 .7-.2 1z"/></svg>
        <span>5555529137</span>
      </li>
      <li class="contact__item">
        <svg class="contact__icon" viewBox="0 0 24 24" fill="var(--accent)" aria-hidden="true"><rect x="2" y="8" width="5" height="14" rx="1"/><path d="M8 9h14v13H8z"/><rect x="10" y="2" width="9" height="6" fill="none" stroke="var(--accent)" stroke-width="2"/><g fill="var(--card)"><rect x="10" y="12" width="2" height="2"/><rect x="14" y="12" width="2" height="2"/><rect x="18" y="12" width="2" height="2"/><rect x="10" y="16" width="2" height="2"/><rect x="14" y="16" width="2" height="2"/><rect x="18" y="16" width="2" height="2"/></g></svg>
        <span>5555529142</span>
      </li>
      <li class="contact__item">
        <svg class="contact__icon" viewBox="0 0 24 24" fill="var(--accent)" aria-hidden="true"><path d="M2 9l10-7 10 7v13H2z"/><path d="M2 9l10 7 10-7" fill="none" stroke="var(--card)" stroke-width="1.5"/><circle cx="12" cy="9" r="3" fill="none" stroke="var(--card)" stroke-width="1.5"/></svg>
        <span>dana@fvzc.info</span>
      </li>
      <li class="contact__item">
        <svg class="contact__icon" viewBox="0 0 24 24" fill="none" stroke="var(--accent)" stroke-width="2" aria-hidden="true"><circle cx="12" cy="12" r="10"/><ellipse cx="12" cy="12" rx="4" ry="10"/><path d="M2 12h20M4 7h16M4 17h16"/></svg>
        <span>www.fvzc.info</span>
      </li>
    </ul>
    <address class="address">517 Marwick Street<br>Harlow Bend, OK 74189</address>
  </section>

  <section class="card card--back" aria-label="Card back">
    <div class="ghost" aria-hidden="true">FVZC</div>
    <div class="brand">
      <span class="brand__square"></span>
      <div class="brand__text">
        <span class="brand__acronym">FVZC</span>
        <span class="brand__name">Ferrant Valley Zoning Council</span>
      </div>
    </div>
  </section>
</main>
</body>
</html>
```